Label / Packaging design for supplements bottle (capsule bottle)

We are a startup supplements company focusing on animal nutrition. The task here is to design the supplement bottles for the product series. Think of bodybuilding supplement packaging more than health&wellness type of packaging.

The brandname is Perch Dynamics

The goal is to have 3 bottles with similar/identical designs but with different color accents (i.e. red for one bottle, yellow for the second, (not green or blue) for the third).

The bottles can either be black theme or white theme. I'll leave it up to the designer.

Final design should communicate bodybuilding (bold fonts preferred)

Logo files below (both SVG and AI files), the insignia can be used independently of the text and slogan, or it can be positioned above brand name or beside it.
*Feel free to change the color of the insignia and text to match your chosen accent color for the bottle!*

Bottle size will be approximately 11.9cm x 6.35cm (Height x circumference) (height is from bottom to mouth opening)
Thus, label size at the moment can be designed 6.30cm x 10cm (L x W)

Target Market(s)

Male, Adult

Industry/Entity Type

It Company

Font styles to use
Sans Serif

Requirements
Must have
• Text: "Performance Enhancing Supplements for Racing Pigeons"
• Essentials
• "240 Capsules"
• Bottle 1:
• Creatine+Carnitine
• Text + Imagery:*see Carnitine Benefits.png
• Bottle 2:
• BCAA
• Text:
• SUPPORT MUSCLE PROTEIN SYNTHESIS
• DECREASE PROTEIN CATABOLISM
• PROMOTE INSULIN SENSITIVITY
• Offset Muscle Breakdown and Increase Muscular Endurance
• ENHANCED RECOVERY FROM EXERCISE
• Promotes Lowered Body Fat Levels, Increased Strength, & Improves Muscle Repair
• (Imagery can use the same as bottle 1 similar to Carnitine Benefits.png)
• Bottle 3:
• Vitamins
• Text: Supports Rigorous Training and Needs To Support Growth and Overall Well-being
• Spaces for Text for:
• 1.) Directions for Use
• 2.) Developed by:
• 3.) Ingredients
Nice to have
• Mosaic/Pattern subtle fading background (e.g. honeycomb etc)
• Prominent "A" "B" "C" on each bottle,
• A for Bulwark Nutrients
• B for BCAA
• C for Taurine/Glutamine Complex
• XYZ Essential Series

```html
<!DOCTYPE html>
<html lang="en">
<head>
<meta charset="utf-8">
<title>Perch Dynamics – BCAA Label</title>
<link href="https://fonts.googleapis.com/css2?family=Anton&family=Oswald:wght@300;400;600&family=Montserrat:wght@700;900&display=swap" rel="stylesheet">
<style>
  :root {
    --label-red: #e31c25;
    --label-red-deep: #b5121a;
    --label-black: #0c0c0c;
    --gold-light: #f3e2b3;
    --gold: #c9a45f;
    --gold-dark: #8a6a32;
    --text-white: #ffffff;
    --tagline-grey: #d9d9d9;
  }
  html, body {
    margin: 0;
    padding: 0;
    width: 1200px;
    height: 641px;
    overflow: hidden;
    background: var(--label-black);
  }
  .label {
    position: relative;
    width: 1200px;
    height: 641px;
    overflow: hidden;
  }
  .label-art {
    position: absolute;
    inset: 0;
    width: 1200px;
    height: 641px;
  }
  .brand {
    position: absolute;
    top: 18px;
    left: 0;
    width: 1200px;
    text-align: center;
  }
  .brand-mark {
    width: 86px;
    height: 86px;
    margin: 0 auto 12px;
    border-radius: 50%;
    background: var(--label-red);
  }
  .brand-name {
    margin: 0;
    font-family: "Montserrat", sans-serif;
    font-weight: 900;
    font-size: 38px;
    line-height: 1;
    letter-spacing: 1px;
    color: var(--text-white);
    text-transform: uppercase;
  }
  .brand-tagline {
    margin-top: 10px;
    font-family: "Oswald", sans-serif;
    font-weight: 400;
    font-size: 14px;
    letter-spacing: 4px;
    color: var(--tagline-grey);
    text-transform: uppercase;
  }
  .headline {
    position: absolute;
    top: 216px;
    left: 0;
    width: 1200px;
    margin: 0;
    text-align: center;
    font-family: "Anton", sans-serif;
    font-weight: 400;
    color: var(--text-white);
    text-transform: uppercase;
    line-height: 1;
  }
  .headline-small { display: block; font-size: 29px; }
  .headline-large { display: block; font-size: 38px; margin-top: 3px; }
  .product-name {
    position: absolute;
    top: 340px;
    left: 0;
    width: 1200px;
    margin: 0;
    text-align: center;
    font-family: "Anton", sans-serif;
    font-weight: 400;
    font-size: 60px;
    line-height: 70px;
    color: var(--text-white);
  }
  .benefits {
    position: absolute;
    top: 427px;
    left: 0;
    width: 1200px;
    margin: 0;
    padding: 0;
    list-style: none;
    text-align: center;
    font-family: "Oswald", sans-serif;
    font-weight: 300;
    font-size: 16px;
    line-height: 21px;
    color: var(--text-white);
    text-transform: uppercase;
  }
  .count {
    position: absolute;
    top: 592px;
    left: 0;
    width: 1200px;
    text-align: center;
    font-family: "Oswald", sans-serif;
    font-size: 36px;
    line-height: 46px;
    color: var(--text-white);
    text-transform: uppercase;
  }
  .count-number { font-weight: 600; }
  .count-unit { font-weight: 300; }
</style>
</head>
<body>
<main class="label">
  <svg class="label-art" viewBox="0 0 1200 641">
    <defs>
      <linearGradient id="gold-sheen" x1="0" y1="0" x2="1" y2="0">
        <stop offset="0" stop-color="#8a6a32"/>
        <stop offset="0.25" stop-color="#f3e2b3"/>
        <stop offset="0.5" stop-color="#c9a45f"/>
        <stop offset="0.75" stop-color="#f3e2b3"/>
        <stop offset="1" stop-color="#8a6a32"/>
      </linearGradient>
      <radialGradient id="red-field" cx="0.5" cy="0.55" r="0.7">
        <stop offset="0" stop-color="#ef2a2f"/>
        <stop offset="1" stop-color="#d0161e"/>
      </radialGradient>
      <linearGradient id="pill-fill" x1="0" y1="0" x2="0" y2="1">
        <stop offset="0" stop-color="#2a2a2a"/>
        <stop offset="0.5" stop-color="#0c0c0c"/>
        <stop offset="1" stop-color="#1d1d1d"/>
      </linearGradient>
    </defs>

    <rect class="red-field" x="0" y="0" width="1200" height="641" fill="url(#red-field)" role="img" aria-label="Subtle red triangular mosaic background pattern"/>

    <path d="M0 140 H318 L380 204 H820 L882 140 H1200" fill="none" stroke="url(#gold-sheen)" stroke-width="8"/>
    <path class="header-band" d="M0 0 H1200 V130 H878 L816 194 H384 L322 130 H0 Z" fill="#0c0c0c"/>

    <path d="M300 352 L360 342 L360 412 L320 420 Z" fill="#b5121a"/>
    <path d="M900 352 L840 342 L840 412 L880 420 Z" fill="#b5121a"/>

    <rect class="benefits-panel" x="322" y="378" width="556" height="190" rx="6" fill="#8a0d12" fill-opacity="0.35"/>

    <rect class="product-pill" x="336" y="334" width="528" height="82" rx="41" fill="url(#pill-fill)" stroke="url(#gold-sheen)" stroke-width="3"/>

    <rect x="0" y="612" width="1200" height="29" fill="url(#gold-sheen)"/>
    <path d="M452 641 L484 586 H716 L748 641 Z" fill="url(#gold-sheen)"/>
    <path class="count-tab" d="M462 641 L490 592 H710 L738 641 Z" fill="#0c0c0c"/>
  </svg>

  <header class="brand">
    <div class="brand-mark"></div>
    <p class="brand-name">Perch Dynamics</p>
    <div class="brand-tagline">Built to Outfly</div>
  </header>

  <h1 class="headline">
    <span class="headline-small">Performance Enhancing</span>
    <span class="headline-large">Supplements for</span>
    <span class="headline-large">Racing Pigeons</span>
  </h1>

  <h2 class="product-name">BCAA</h2>

  <ul class="benefits">
    <li>-Support Muscle Protein Synthesis</li>
    <li>- Decrease Protein Catabolism</li>
    <li>- Promote Insulin Sensitivity</li>
    <li>- Offset Muscle Breakdown and Increase Muscular Endurance</li>
    <li>- Enhanced Recovery from Exercise</li>
    <li>- Promotes Lowered Body Fat Levels, Increased Strength, &amp; Improves Muscle Repair</li>
  </ul>

  <div class="count"><span class="count-number">240</span> <span class="count-unit">Capsules</span></div>
</main>
</body>
</html>
```